Postcard Design

www.lirvo.com.au
i am an occupational therapist and professionally trained coach. i work with children, parents and disability service providers to achieve brilliant outcomes for children with special needs.
http://www.lirvo.com.au/service/for-families
I need a postcard to give parents to promote our family service coaching service
A family service coach will work with you to set specific goals for your child, build a dream team, design and manage your child's highly effective therapy and educational team to ensure brilliant outcomes for your child..
KORLU - you have done my business card previously. they were great thank you.

```html
<!DOCTYPE html>
<html lang="en">
<head>
<meta charset="utf-8">
<title>Family Service Coach Postcard</title>
<link rel="stylesheet" href="https://fonts.googleapis.com/css2?family=Bebas+Neue&display=swap">
<style>
  :root {
    --paper: #ffffff;
    --ink-heading: #3b4060;
    --ink-label: #2d4c8a;
    --circle-blue: #5a86c4;
    --band-blue: #5f82b8;
    --band-text: #ffffff;
    --rule-grey: #dcdcdc;
    --stamp-grey: #d6d6d6;
    --photo-dark: #2b3442;
    --photo-mid: #56606c;
    --photo-light: #9aa3ad;
  }
  * { margin: 0; padding: 0; box-sizing: border-box; }
  html, body {
    width: 1200px;
    height: 930px;
    overflow: hidden;
    background: var(--paper);
  }
  .postcard {
    position: relative;
    width: 1200px;
    height: 930px;
    background: var(--paper);
    font-family: "Bebas Neue", "Arial Narrow", sans-serif;
  }
  .photo-area {
    position: absolute;
    left: 0; top: 0;
    width: 579px; height: 387px;
    background: radial-gradient(ellipse at 45% 45%, var(--photo-light) 0%, var(--photo-mid) 45%, var(--photo-dark) 100%);
  }
  .services-heading {
    position: absolute;
    left: 0; top: 396px;
    width: 579px;
    text-align: center;
    font-size: 42px;
    letter-spacing: 0.5px;
    color: var(--ink-heading);
  }
  .service-steps {
    position: absolute;
    left: 0; top: 452px;
    width: 579px; height: 110px;
  }
  .service-labels {
    position: absolute;
    left: 0; top: 556px;
    width: 579px; height: 80px;
  }
  .service-label {
    position: absolute;
    top: 0;
    width: 140px;
    margin-left: -70px;
    text-align: center;
    font-size: 28px;
    line-height: 24px;
    color: var(--ink-label);
  }
  .web-band {
    position: absolute;
    left: 0; top: 660px;
    width: 579px; height: 105px;
    background: var(--band-blue);
    display: flex;
    align-items: center;
    justify-content: center;
    font-size: 33px;
    letter-spacing: 0.3px;
    color: var(--band-text);
  }
  .stamp-box {
    position: absolute;
    left: 907px; top: 30px;
    width: 266px; height: 265px;
    border: 2px solid var(--stamp-grey);
  }
  .address-line {
    position: absolute;
    left: 645px;
    width: 496px;
    height: 2px;
    background: var(--rule-grey);
  }
</style>
</head>
<body>
<main class="postcard">
  <div class="photo-area" role="img" aria-label="Photo of several hands joining coloured puzzle pieces together"></div>

  <h1 class="services-heading">A Family Service Coach Provides:</h1>

  <svg class="service-steps" viewBox="0 0 579 110" aria-hidden="true">
    <g stroke="var(--circle-blue)" stroke-width="2" fill="var(--circle-blue)">
      <line x1="145" y1="50" x2="182" y2="50"/><circle cx="174" cy="50" r="4"/>
      <line x1="274" y1="50" x2="310" y2="50"/><circle cx="302" cy="50" r="4"/>
      <line x1="402" y1="50" x2="442" y2="50"/><circle cx="434" cy="50" r="4"/>
    </g>
    <g fill="var(--circle-blue)">
      <circle cx="99" cy="50" r="46"/>
      <circle cx="228" cy="50" r="46"/>
      <circle cx="356" cy="50" r="46"/>
      <circle cx="488" cy="50" r="46"/>
    </g>
    <!-- target with arrow -->
    <g fill="none" stroke="#fff" stroke-width="4">
      <circle cx="103" cy="46" r="24"/>
      <circle cx="103" cy="46" r="14"/>
    </g>
    <circle cx="103" cy="46" r="5" fill="#fff"/>
    <path d="M103 46 L80 69 M76 73 l6 -16 l10 10 z" stroke="#fff" stroke-width="5" fill="#fff" stroke-linejoin="round"/>
    <!-- group of people -->
    <g fill="#fff">
      <circle cx="228" cy="27" r="8"/>
      <rect x="219" y="38" width="18" height="38" rx="6"/>
      <circle cx="207" cy="33" r="6.5"/>
      <rect x="199" y="42" width="15" height="30" rx="5"/>
      <circle cx="249" cy="33" r="6.5"/>
      <rect x="242" y="42" width="15" height="30" rx="5"/>
    </g>
    <!-- clipboard with sheet -->
    <g fill="none" stroke="#fff" stroke-width="3.5" stroke-linejoin="round">
      <rect x="335" y="28" width="32" height="46" rx="3"/>
      <rect x="345" y="23" width="13" height="9" rx="2" fill="#fff"/>
      <path d="M350 40 l24 -6 l8 36 l-26 7 z" fill="var(--circle-blue)"/>
      <path d="M356 46 l16 -4 M358 53 l16 -4 M360 60 l16 -4"/>
    </g>
    <!-- graduation cap -->
    <g fill="#fff">
      <path d="M488 28 L520 42 L488 56 L456 42 Z"/>
      <path d="M470 50 v13 c10 8 26 8 36 0 v-13 l-18 8 z"/>
      <rect x="515" y="43" width="3" height="20"/>
    </g>
  </svg>

  <div class="service-labels">
    <p class="service-label" style="left:95px;top:2px;">Set Goals</p>
    <p class="service-label" style="left:228px;">Build a<br>Dream Team</p>
    <p class="service-label" style="left:361px;">Design and<br>Manage<br>Therapy</p>
    <p class="service-label" style="left:492px;">Educational<br>Team</p>
  </div>

  <div class="web-band">www.lirvo.com.au/service/for-families</div>

  <div class="stamp-box" aria-label="Stamp area"></div>
  <div class="address-line" style="top:419px;"></div>
  <div class="address-line" style="top:503px;"></div>
  <div class="address-line" style="top:585px;"></div>
  <div class="address-line" style="top:668px;"></div>
</main>
</body>
</html>
```